New Property Management Division

We need a flyer designed to discuss our recently launched Property Management division. We are an executive recruiting firm based in Dallas dedicated to the commercial real estate industry. We have historically only worked on investment related positions (acquisitions, development, asset management, etc.) The Property Management division represents our entry into operational positions. We will be placing Property Managers, Leasing Managers, Building Engineers and Property Accountants. The final design should incorporate our existing look and feel - but open to advancing that look as well. I have the logo in vector formats.
Target Market(s)
Commercial Real Estate firms that own (acquire or develop) real estate buildings (retail, office, apartments, industrial, self-storage, etc.).
Industry/Entity Type
Recruitment
Number of Pages Required
1 page
Font styles to use
Other font styles liked:
- We use Calibri a lot
Colors
Designer to choose colors to be used in the design.
Requirements
Must have
- Images of buildings (office, retail, apartments, etc.)
- Description of the types of positions this division will place (Property Managers, Leasing Managers, Building Engineers and Property Accountants)
- Pic and/or bio of the Vice President running property management division (Dale Farrow)
Should not have
- Our clients are professional investors so would not like to see images that are too whimsical.

```html
<!DOCTYPE html>
<html lang="en">
<head>
<meta charset="utf-8">
<title>Harlow Executive Recruiting – Property Management Division</title>
<link href="https://fonts.googleapis.com/css2?family=Carlito:wght@400;700&family=Kalam:wght@400&display=swap" rel="stylesheet">
<style>
  :root{
    --page-bg:#e4e4e4;
    --paper:#f7f7f7;
    --blue:#3a82c6;
    --blue-dark:#2a64a3;
    --blue-light:#5b9bd6;
    --orange:#c8532b;
    --ink:#2d3a4a;
    --white:#ffffff;
  }
  *{box-sizing:border-box;margin:0;padding:0}
  html,body{width:1200px;height:900px;overflow:hidden}
  body{background:var(--page-bg);font-family:"Carlito",Calibri,Arial,sans-serif;color:var(--ink)}
  .flyer{position:absolute;left:270px;top:20px;width:660px;height:860px;background:var(--paper);overflow:hidden;box-shadow:0 6px 18px rgba(0,0,0,.12)}

  .brand{position:absolute;right:36px;top:30px;display:flex;align-items:center;gap:12px}
  .brand-mark{width:30px;height:30px;background:var(--blue-dark)}
  .brand-name{font-size:34px;letter-spacing:8px;color:var(--ink);font-weight:400}

  .hero-photo{position:absolute;left:0;top:100px;width:660px;height:300px;
    background:linear-gradient(120deg,#dfe6ee 0%,#c4cfdb 45%,#8aa3bd 100%)}
  .hero-shapes{position:absolute;left:0;top:100px;width:660px;height:340px}
  .site-url{position:absolute;left:26px;top:130px;color:var(--white);font-size:15px}
  .tagline{position:absolute;right:22px;top:152px;color:var(--white)}
  .tagline-intro{font-size:17px;background:var(--blue);padding:4px 10px;display:inline-block}
  .tagline-key{display:inline-block;background:var(--orange);font-size:27px;padding:0 10px;margin-top:4px}
  .tagline-amp{font-size:27px;padding-left:10px;color:var(--white)}
  .tagline-amp span{background:var(--orange);padding:0 8px}

  .script{font-family:"Kalam","Segoe Print",cursive}
  .experience{position:absolute;left:340px;top:408px;width:305px}
  .experience h2{font-size:30px;color:var(--blue);font-weight:400;border-bottom:2px solid var(--blue);display:inline-block;padding-right:10px;line-height:1.2}
  .experience-list{display:grid;grid-template-columns:1fr 1fr;gap:0 10px;margin-top:10px;list-style:none}
  .experience-list li{font-size:13px;line-height:19px;color:var(--ink);display:flex;align-items:center;gap:6px;white-space:nowrap}
  .tick{width:10px;height:10px;flex:none}

  .about{position:absolute;left:36px;top:438px;width:280px}
  .about h2{font-size:32px;color:var(--orange);font-weight:400;line-height:1.1}
  .about p{margin-top:10px;color:var(--orange);font-size:14px;line-height:18px}

  .leader{position:absolute;left:120px;top:650px;width:180px;text-align:center}
  .leader-photo{width:100px;height:100px;border-radius:50%;border:4px solid var(--orange);margin:0 auto;
    background:radial-gradient(circle at 50% 40%,#d9dde2,#8e97a3)}
  .leader-name{margin-top:8px;font-size:18px;color:var(--blue-dark)}
  .leader-role{font-size:13px;line-height:16px;color:var(--blue-dark)}

  .positions{position:absolute;left:340px;top:600px;width:320px;height:260px;border-left:6px solid var(--orange);background:var(--blue)}
  .positions-base{position:absolute;left:0;bottom:0;width:100%;height:80px;background:var(--blue-light)}
  .positions h2{position:absolute;left:22px;top:34px;font-size:26px;line-height:28px;color:var(--white);font-weight:400}
  .position-list{position:absolute;left:140px;top:24px;list-style:none}
  .position-list li{color:var(--white);font-size:15px;line-height:24px;display:flex;align-items:center;gap:10px;white-space:nowrap}
  .position-list li::before{content:"";width:10px;height:10px;border-radius:50%;background:var(--orange);border:2px solid var(--white)}
  .contact-lines{position:absolute;left:140px;top:126px;list-style:none}
  .contact-lines li{color:var(--white);font-size:12px;line-height:18px;display:flex;align-items:center;gap:8px;white-space:nowrap}
  .contact-lines svg{width:9px;height:9px;flex:none}
  .contact-badge{position:absolute;left:48px;top:158px;width:62px;height:62px;border-radius:50%;background:var(--orange);border:3px solid var(--white);
    color:var(--white);font-size:14px;font-weight:700;display:flex;align-items:center;justify-content:center}
</style>
</head>
<body>
<main class="flyer">
  <header class="brand">
    <span class="brand-mark"></span>
    <span class="brand-name">HARLOW</span>
  </header>

  <div class="hero-photo" role="img" aria-label="Photo of a smiling team of five real estate professionals in business attire"></div>
  <svg class="hero-shapes" viewBox="0 0 660 340" aria-hidden="true">
    <polygon points="0,22 190,22 170,56 0,56" fill="#3a82c6"/>
    <polygon points="190,22 230,22 170,56" fill="#2a64a3"/>
    <polygon points="300,270 660,205 660,300 330,300" fill="#3a82c6"/>
    <polygon points="300,270 330,300 300,322" fill="#2a64a3"/>
  </svg>
  <div class="site-url">www.harlowrecruiting.com</div>
  <div class="tagline">
    <div class="tagline-intro">At the Intersection of</div><br>
    <div class="tagline-key">Real Estate</div>
    <div class="tagline-amp">&amp; <span>Finance</span></div>
  </div>

  <section class="experience">
    <h2 class="script">Experiences</h2>
    <ul class="experience-list">
      <li><svg class="tick" viewBox="0 0 10 10"><path d="M1 5l3 3 5-7" stroke="#2a64a3" stroke-width="2" fill="none"/></svg>Acquisitions</li>
      <li><svg class="tick" viewBox="0 0 10 10"><path d="M1 5l3 3 5-7" stroke="#2a64a3" stroke-width="2" fill="none"/></svg>Development</li>
      <li><svg class="tick" viewBox="0 0 10 10"><path d="M1 5l3 3 5-7" stroke="#2a64a3" stroke-width="2" fill="none"/></svg>Asset Management</li>
      <li><svg class="tick" viewBox="0 0 10 10"><path d="M1 5l3 3 5-7" stroke="#2a64a3" stroke-width="2" fill="none"/></svg>Property Management</li>
      <li><svg class="tick" viewBox="0 0 10 10"><path d="M1 5l3 3 5-7" stroke="#2a64a3" stroke-width="2" fill="none"/></svg>Banking/Lending</li>
      <li><svg class="tick" viewBox="0 0 10 10"><path d="M1 5l3 3 5-7" stroke="#2a64a3" stroke-width="2" fill="none"/></svg>Accounting/CFO</li>
      <li><svg class="tick" viewBox="0 0 10 10"><path d="M1 5l3 3 5-7" stroke="#2a64a3" stroke-width="2" fill="none"/></svg>Brokerage</li>
      <li><svg class="tick" viewBox="0 0 10 10"><path d="M1 5l3 3 5-7" stroke="#2a64a3" stroke-width="2" fill="none"/></svg>Leasing Manager</li>
      <li><svg class="tick" viewBox="0 0 10 10"><path d="M1 5l3 3 5-7" stroke="#2a64a3" stroke-width="2" fill="none"/></svg>Capital Markets</li>
      <li><svg class="tick" viewBox="0 0 10 10"><path d="M1 5l3 3 5-7" stroke="#2a64a3" stroke-width="2" fill="none"/></svg>Construction</li>
      <li><svg class="tick" viewBox="0 0 10 10"><path d="M1 5l3 3 5-7" stroke="#2a64a3" stroke-width="2" fill="none"/></svg>Investment Sales</li>
      <li><svg class="tick" viewBox="0 0 10 10"><path d="M1 5l3 3 5-7" stroke="#2a64a3" stroke-width="2" fill="none"/></svg>Workouts (Loan &amp; REO)</li>
    </ul>
  </section>

  <section class="about">
    <h2 class="script">What We Do</h2>
    <p>HARLOW | Executive Recruiting is a professional search firm focused exclusively on the hiring needs of commercial real estate companies. HARLOW is more than a placement firm. We are trusted advisors who partner with our clients, offer focused representation, help develop organizations - and get real results.</p>
  </section>

  <section class="leader">
    <div class="leader-photo" role="img" aria-label="Portrait photo of Dale Farrow, Vice President"></div>
    <div class="leader-name">Dale Farrow</div>
    <div class="leader-role">Vice President<br>Property Management Division</div>
  </section>

  <section class="positions">
    <div class="positions-base"></div>
    <h2>Types of<br>Position</h2>
    <ul class="position-list">
      <li>Leasing Managers</li>
      <li>Property Managers</li>
      <li>Building Engineers</li>
      <li>Property Accountants</li>
    </ul>
    <ul class="contact-lines">
      <li><svg viewBox="0 0 10 10"><path d="M2 1l2 2-1 1.5a6 6 0 0 0 2.5 2.5L7 6l2 2-1.5 1.5C4 9 1 6 .5 2.5z" fill="#fff"/></svg>214-555-0183</li>
      <li><svg viewBox="0 0 10 10"><rect x="0.5" y="2" width="9" height="6" fill="#fff"/><path d="M.5 2l4.5 3.5L9.5 2" stroke="#3a82c6" fill="none"/></svg>jordan@harlowrecruiting.com</li>
      <li><svg viewBox="0 0 10 10"><path d="M5 0a3.5 3.5 0 0 0-3.5 3.5C1.5 6 5 10 5 10s3.5-4 3.5-6.5A3.5 3.5 0 0 0 5 0z" fill="#fff"/></svg>www.harlowrecruiting.com</li>
    </ul>
    <div class="contact-badge">Contact</div>
  </section>
</main>
</body>
</html>
```